CD cover - Mantras: Endless Light Ahead

Welcome!

The album contains acoustic music with positive and affirmative lyrics.

Here's a medley of some songs.
https://files.sharevaultcdn.example/u/83104576/bela_moritz_endless_light_ahead_20150220.mp3

This music and life style is about enjoying ourselves and this game we call life. Respect, gratitude, love, forgiveness, simplicity, together these lead to a happy, blissful life. If the potential listener - when looking at the cover - gets this message, than it's perfect. Just make it simple, playful, beautiful. :)

BUT PLEASE AVOID CLICHÉS!! Come up with something original! Thank you!

Note: the front cover in case of online purchase of the album will be shown on a cell-phone for example. If the image is complicated and too detailed, it won't look like something.

The CD cover project has 4 parts:
1. CD cover front outside
2. CD cover front inside (track list)
3. CD cover back
4. CD (print on the disc)

The performer: Bela Moritz (logo attached). Please use the logo with the original colors and design the cover to go well with it.

Album title: Mantras: Endless Light Ahead
All my upcoming albums are going to be called "Mantras: something"

Track list:
1. Morning Tide (3:52)
2. Open Sky (3:44)
3. Lantern Glow (4:31)
4. Quiet River (2:57)
5. Kindness (3:05)
6. Feather (3:36)
7. Sunlit Path (3:27)
8. Thank You (4:08)
9. Calm & Clear (3:34)
10. New Horizon (4:11)
11. Stillness (4:42)
12. One Sky (4:15)

All songs written by Bela Moritz
Copyright Belasound 2015.
www.belasound.example

I am going to need the cover in RGB format.

That's pretty much it. If I missed something important, mail me without hesitation! Enjoy! :)

Target Market(s)

New Age spiritual people, positive thinking people.

Industry/Entity Type

Cell Phone

Requirements
Must have
• Easy to read text and logo. I'm still building the brand.
Nice to have
• Light colors
Should not have
• Any kind of negativity at all.

```html
<!DOCTYPE html>
<html lang="en">
<head>
<meta charset="utf-8">
<title>Mantras: Endless Light Ahead – Track List</title>
<link href="https://fonts.googleapis.com/css2?family=Cinzel:wght@400;500&display=swap" rel="stylesheet">
<style>
  :root {
    --paper: #fbf7f8;
    --blush: #eedfe5;
    --mauve: #d4b9c9;
    --ink: #3b3538;
    --gold: #f2b230;
  }
  html, body {
    margin: 0;
    padding: 0;
    width: 1200px;
    height: 1200px;
    overflow: hidden;
    background: var(--paper);
  }
  .cover {
    position: relative;
    width: 1200px;
    height: 1200px;
    overflow: hidden;
    font-family: "Cinzel", "Times New Roman", serif;
    color: var(--ink);
  }
  .cover-photo {
    position: absolute;
    inset: 0;
    background:
      radial-gradient(ellipse 420px 90px at 560px 860px, rgba(255,255,255,0.55), rgba(255,255,255,0) 70%),
      radial-gradient(ellipse 500px 160px at 420px 880px, rgba(176,140,180,0.55), rgba(176,140,180,0) 75%),
      radial-gradient(ellipse 240px 420px at 860px 420px, rgba(200,210,235,0.45), rgba(200,210,235,0) 70%),
      radial-gradient(ellipse 130px 110px at 1070px 170px, rgba(140,120,200,0.35), rgba(140,120,200,0) 75%),
      linear-gradient(180deg, #ffffff 0%, #fbf5f7 30%, var(--blush) 60%, var(--mauve) 100%);
  }
  .brand {
    position: absolute;
    left: 150px;
    top: 64px;
    display: flex;
    flex-direction: column;
    align-items: center;
  }
  .brand-dot {
    width: 60px;
    height: 60px;
    border-radius: 50%;
    background: var(--gold);
  }
  .brand-name {
    margin-top: 16px;
    font-size: 30px;
    font-weight: 400;
    letter-spacing: 1px;
    line-height: 1;
  }
  .album-title {
    position: absolute;
    left: 150px;
    top: 242px;
    margin: 0;
    font-size: 30px;
    font-weight: 400;
    line-height: 1;
    letter-spacing: 1px;
  }
  .track-list {
    position: absolute;
    left: 150px;
    top: 298px;
    margin: 0;
    padding: 0;
    list-style: none;
    font-size: 17px;
    line-height: 24px;
    letter-spacing: 0.5px;
  }
  .credits {
    position: absolute;
    left: 150px;
    top: 620px;
    margin: 0;
    font-size: 15px;
    line-height: 24px;
    letter-spacing: 0.5px;
  }
</style>
</head>
<body>
  <main class="cover">
    <div class="cover-photo" role="img" aria-label="Soft pastel photograph of an open palm reaching in from the left with wisps of coloured smoke rising above it"></div>

    <div class="brand">
      <span class="brand-dot" aria-hidden="true"></span>
      <span class="brand-name">Bela Moritz</span>
    </div>

    <h1 class="album-title">Mantras: Endless Light Ahead</h1>

    <ol class="track-list">
      <li>1. Morning Tide (3:52)</li>
      <li>2. Open Sky (3:44)</li>
      <li>3. Lantern Glow (4:31)</li>
      <li>4. Quiet River (2:57)</li>
      <li>5. Kindness (3:05)</li>
      <li>6. Feather (3:36)</li>
      <li>7. Sunlit Path (3:27)</li>
      <li>8. Thank You (4:08)</li>
      <li>9. Calm &amp; Clear (3:34)</li>
      <li>10. New Horizon (4:11)</li>
      <li>11. Stillness (4:42)</li>
      <li>12. One Sky (4:15)</li>
    </ol>

    <p class="credits">
      All songs written by Bela Moritz<br>
      Copyright Belasound 2015.<br>
      www.belasound.example
    </p>
  </main>
</body>
</html>
```